依頼詳細
PCとスマホデザインの両方納品をいただきますが、
まずはデザインイメージが確認しやすいPCページのみの提案をお願いします。
スマホページは当選者に納品時にお願いしたいと思います。
スマホサイズについて、表示は横幅375pxで作成し、
デザインデータは2倍の横幅750pxのカンバスサイズで作成してください。
(Retinaディスプレイに対応するため)
レスポンシブウェブデザインを意識したデザインでお願いします。

■サイトマップ
添付の画面遷移図をご確認ください。

■参考サイト
http://hoshizora-tetsuko.co.jp/

■内容について
鋳造部品等を製作する会社のサイトリニューアルになります。
既存サイト
http://www.senbeiseiko.com/kiyora/index.html

■素材写真
画像データについては、フリー素材から流用して
イメージ画像に当て込んでください。
足りない場合は、一旦他のサイトの写真をサンプルとして
入れてください。(サンプルなどの表記をお願いします)
また、購入が必要な写真などを利用した場合、
価格とサイト名を教えてください。

また、Lumera Photosで定期契約をしていますので、
Lumera Photosの画像は使用できます。
デザイン時はカンプ画像をお入れいただきますようお願いします。

■ワイヤーフレーム
https://mock.wirevista.net/view/1a2b3c4d-5e6f-4a7b-8c9d-0e1f2a3b4c5d-8812/?fullscreen
コンテンツの構成としてワイヤーフレームを作成しましたが
必ずしもワイヤーフレームの通りではなくて大丈夫です。
TOPページに配置するコンテンツを見ていただき、デザインは
デザイナーの皆様におまかせしたいと思います。

----------------------------------------------------------------------------
【制作物に対するお願い】

■フォントについて
・無料で使えるフォントで作成をお願いします。
・OSに紐づくフォントの使用は控えていただければと思います (ヒラギノなど)

ページ数
1ページ
希望イメージ
シンプル 複雑
単色 カラフル
暗い 明るい
日常 高級
遊び心 厳粛
未来的 伝統的
女性的 男性的
希望する色
アクセントカラー:茶色、もしくは青色
納品ファイル
• 高解像度JPG (.jpg)
• イラストレーター形式 (.ai)
• フォトショップ形式 (.psd)
補足説明
上記のいずれか1つ(アウトラインありとなしの2つ)と高解像度JPGを納品お願いします。
adobe XDでの納品も可能です。

```html
<!DOCTYPE html>
<html lang="ja">
<head>
<meta charset="utf-8">
<title>清良伸銅株式会社</title>
<link href="https://fonts.googleapis.com/css2?family=Noto+Sans+JP:wght@400;500;700&family=Noto+Serif+JP:wght@600;700&family=Roboto:wght@400;500;700&display=swap" rel="stylesheet">
<style>
:root{
  --blue:#2b5cad;
  --blue-dark:#1f4789;
  --ink:#222;
  --text:#444;
  --muted:#777;
  --gray-bg:#eef0f3;
  --line:#d8dbe0;
  --navy:#232a36;
  --white:#fff;
}
*{margin:0;padding:0;box-sizing:border-box}
html,body{width:1200px;height:4584px;overflow:hidden}
body{font-family:"Noto Sans JP",sans-serif;color:var(--text);background:var(--white);position:relative}
section,header,footer{position:relative;width:1200px;overflow:hidden}
.en{font-family:"Roboto",sans-serif}
.photo{position:absolute}

/* header */
.site-header{height:104px;display:flex;align-items:center;justify-content:space-between;padding-left:28px;background:var(--white)}
.logo{font-family:"Noto Serif JP",serif;font-weight:700;font-size:28px;color:var(--ink);letter-spacing:.04em}
.gnav{display:flex;height:100%;align-items:center}
.gnav a{font-size:15px;font-weight:500;color:var(--ink);text-decoration:none;margin-right:34px}
.gnav a.current{color:var(--blue)}
.gnav .btn-contact{height:100%;width:150px;background:var(--blue);color:var(--white);display:flex;align-items:center;justify-content:center;margin:0}

/* hero */
.hero{height:616px}
.hero .photo{inset:0;background:radial-gradient(ellipse at 68% 40%,#f08a2a 0%,#b8461a 18%,#4a2a22 42%,#1d1d22 75%)}
.hero-copy{position:absolute;left:168px;top:250px;color:var(--white)}
.hero-copy .en{font-size:26px;letter-spacing:.08em;border-bottom:1px solid rgba(255,255,255,.6);padding-bottom:14px;width:260px}
.hero-copy h1{font-size:40px;font-weight:700;line-height:1.5;margin-top:18px;letter-spacing:.04em}

/* section title */
.sec-title{text-align:center;color:var(--blue-dark)}
.sec-title h2{font-size:32px;font-weight:700;letter-spacing:.06em}
.sec-title .en{display:block;font-size:14px;color:var(--ink);letter-spacing:.15em;margin-top:4px}

.btn-more{display:inline-flex;align-items:center;justify-content:space-between;width:208px;height:50px;background:var(--blue);color:var(--white);font-size:14px;padding:0 22px;text-decoration:none;font-family:"Roboto",sans-serif;letter-spacing:.06em}

/* about */
.about{height:740px}
.about .sec-title{padding-top:96px}
.about-body{position:absolute;left:168px;top:330px;width:420px}
.about-body h3{font-size:27px;color:var(--blue-dark);line-height:1.5;font-weight:700}
.about-body p{font-size:14px;line-height:2;margin-top:28px}
.about-body .btn-more{margin-top:40px}
.about .photo{left:620px;top:328px;width:470px;height:280px;background:linear-gradient(135deg,#d7dadf,#8d949c 55%,#c4c8cd)}

/* products */
.products{height:560px;background:var(--gray-bg)}
.products .sec-title{padding-top:96px}
.product-list{position:absolute;left:170px;top:254px;display:flex;gap:40px}
.product{width:260px}
.product .photo{position:relative;width:260px;height:200px}
.product h3{font-size:17px;color:var(--blue-dark);text-align:center;margin-top:14px;font-weight:700}
.product p{font-size:12px;line-height:1.7;margin-top:8px}
.p1{background:linear-gradient(135deg,#e6ddc4,#c7a55a)}
.p2{background:linear-gradient(135deg,#e2cfc0,#c57948)}
.p3{background:linear-gradient(135deg,#d6d8da,#8b8f94)}

/* works */
.works{height:760px;background:var(--white)}
.works .deco{position:absolute;inset:0}
.works .sec-title{padding-top:110px;position:relative}
.works .photo{left:280px;top:240px;width:310px;height:360px;background:linear-gradient(160deg,#9aa2aa,#4d545c 55%,#2a2f35)}
.works-body{position:absolute;left:620px;top:300px;width:380px}
.works-body h3{font-size:25px;color:var(--blue-dark);line-height:1.5;font-weight:700}
.works-body p{font-size:13px;line-height:1.9;margin-top:20px}
.works-body .btn-more{margin-top:40px;margin-left:200px}

/* recruit */
.recruit{height:660px}
.recruit .photo{inset:0;background:linear-gradient(180deg,#2c3038,#1b1e24 60%,#3a3e44)}
.recruit .sec-title{padding-top:150px;position:relative;color:var(--white)}
.recruit .sec-title .en{color:var(--white)}
.recruit-box{position:absolute;left:260px;top:260px;width:680px;height:340px;background:var(--white);text-align:center;padding-top:44px}
.recruit-box h3{font-size:22px;color:var(--blue-dark);font-weight:700}
.recruit-box p{font-size:13px;line-height:2;margin-top:22px}
.recruit-box .btn-more{margin-top:34px}

/* news */
.news{height:460px}
.news-head{position:absolute;left:168px;top:90px}
.news-head h2{font-size:22px;color:var(--blue-dark);font-weight:700}
.news-head .en{font-size:12px;letter-spacing:.15em;color:var(--ink)}
.news-head .btn-list{display:inline-flex;align-items:center;justify-content:space-between;width:130px;height:32px;border:1px solid var(--ink);font-size:11px;padding:0 12px;margin-top:24px;color:var(--ink);text-decoration:none}
.news-list{position:absolute;left:368px;top:80px;width:660px;list-style:none}
.news-list li{border-bottom:1px solid var(--line);padding:14px 0 16px}
.news-list time{font-size:13px;color:var(--ink);display:block;font-family:"Roboto",sans-serif}
.news-list p{font-size:13px;margin-top:8px}

/* contact */
.contact{height:428px}
.contact .photo{left:170px;top:40px;width:860px;height:300px;background:linear-gradient(120deg,#2a2624,#5a3a26 55%,#c26a2a 80%,#3a2a22)}
.contact-inner{position:absolute;left:170px;top:40px;width:860px;height:300px;text-align:center;color:var(--white)}
.contact-inner h2{font-family:"Roboto",sans-serif;font-size:30px;letter-spacing:.12em;margin-top:42px;font-weight:700}
.contact-inner .lead{font-size:13px;margin-top:12px}
.contact-boxes{display:flex;gap:20px;justify-content:center;margin-top:38px}
.cbox{width:360px;height:86px;background:var(--white);display:flex;align-items:center;justify-content:center;gap:14px;color:var(--ink)}
.cbox .tel{font-family:"Roboto",sans-serif;font-size:26px;font-weight:700;color:var(--ink);line-height:1.1}
.cbox small{display:block;font-size:10px;color:var(--muted)}
.cbox .mail{font-size:16px;font-weight:500}
.to-top{position:absolute;right:110px;top:360px;width:48px;height:48px;background:var(--blue);display:flex;align-items:center;justify-content:center}

/* footer */
.site-footer{height:256px;background:var(--navy);color:var(--white)}
.site-footer .logo{position:absolute;left:190px;top:78px;color:var(--white);font-size:24px}
.fnav{position:absolute;left:578px;top:70px;width:440px;display:flex;flex-wrap:wrap;gap:14px 22px;font-size:12px}
.fnav a{color:var(--white);text-decoration:none}
.copy{position:absolute;left:0;right:0;top:200px;text-align:center;font-size:11px;color:#b7bcc5;font-family:"Roboto",sans-serif}
</style>
</head>
<body>

<header class="site-header">
  <div class="logo">清良伸銅株式会社</div>
  <nav class="gnav">
    <a class="current" href="#">会社案内</a>
    <a href="#">製造案内</a>
    <a href="#">製品紹介</a>
    <a href="#">採用情報</a>
    <a class="btn-contact" href="#">お問い合わせ</a>
  </nav>
</header>

<section class="hero">
  <div class="photo" role="img" aria-label="溶けた金属を流し込む鋳造現場の写真"></div>
  <div class="hero-copy">
    <div class="en">Kiyora Shindo</div>
    <h1>確かな技術とモノ造りで<br>ご要望にお応え致します。</h1>
  </div>
</section>

<section class="about">
  <div class="sec-title"><h2>清良伸銅とは</h2><span class="en">ABOUT US</span></div>
  <div class="about-body">
    <h3>モノ造りのプロとして、<br>確かな技術でお答えします</h3>
    <p>清良伸銅株式会社は創業以来70年以上に渡り、鋳造品を製作してきました。時代のニーズに応えつつ、これまで受け継いできた職人の技を継承し、社員全員一丸となって安全な製品・技術・製品・サービスを常に追求します。</p>
    <a class="btn-more" href="#">READ MORE<svg width="34" height="8" viewBox="0 0 34 8"><path d="M0 7h32L26 1" fill="none" stroke="#fff" stroke-width="1.2"/></svg></a>
  </div>
  <div class="photo" role="img" aria-label="金属加工部品が並ぶ写真"></div>
</section>

<section class="products">
  <div class="sec-title"><h2>製品紹介</h2><span class="en">PRODUCTS</span></div>
  <div class="product-list">
    <div class="product">
      <div class="photo p1" role="img" aria-label="真鍮製の機械部品の写真"></div>
      <h3>機械部品</h3>
      <p>こちらに製品の説明が入ります。テキストテキストテキストテキスト（サンプルテキストです）</p>
    </div>
    <div class="product">
      <div class="photo p2" role="img" aria-label="銅製の電気部品の写真"></div>
      <h3>電気部品</h3>
      <p>こちらに製品の説明が入ります。テキストテキストテキストテキスト（サンプルテキストです）</p>
    </div>
    <div class="product">
      <div class="photo p3" role="img" aria-label="金属製のその他部品の写真"></div>
      <h3>その他の製品</h3>
      <p>こちらに製品の説明が入ります。テキストテキストテキストテキスト（サンプルテキストです）</p>
    </div>
  </div>
</section>

<section class="works">
  <svg class="deco" width="1200" height="760" viewBox="0 0 1200 760" aria-hidden="true">
    <polygon points="0,0 360,0 0,300" fill="#f1f2f5"/>
    <polygon points="1200,60 1200,560 820,760 700,760" fill="#f1f2f5"/>
    <polygon points="0,520 260,760 0,760" fill="#f5f6f8"/>
  </svg>
  <div class="sec-title"><h2>製造案内</h2><span class="en">WORKS</span></div>
  <div class="photo" role="img" aria-label="精密に削り出された金属シャフトの写真"></div>
  <div class="works-body">
    <h3>充実した設備と確かな技術で<br>お客様のご要望にお応えします。</h3>
    <p>清良伸銅株式会社は、自動生産ラインでは困難な製造品を、これまで培ってきた技術で製造いたします。お客様のご要望に応じて小さな製品から大型製品まで幅広く対応いたします。</p>
    <a class="btn-more" href="#">READ MORE<svg width="34" height="8" viewBox="0 0 34 8"><path d="M0 7h32L26 1" fill="none" stroke="#fff" stroke-width="1.2"/></svg></a>
  </div>
</section>

<section class="recruit">
  <div class="photo" role="img" aria-label="工場内で作業する機械設備の写真"></div>
  <div class="sec-title"><h2>採用情報</h2><span class="en">RECRUIT</span></div>
  <div class="recruit-box">
    <h3>清良伸銅ではともに働く仲間を募集しております。</h3>
    <p>清良伸銅株式会社では、鋳造品の製造から加工まで、一貫生産で対応しております。<br>お客様の様々なご要望にお応えするべく、ともに働く仲間を募集しています。<br>当社での人材教育に力を入れており、未経験の方も一から指導し、<br>「職人」に育てる環境があります。</p>
    <a class="btn-more" href="#">READ MORE<svg width="34" height="8" viewBox="0 0 34 8"><path d="M0 7h32L26 1" fill="none" stroke="#fff" stroke-width="1.2"/></svg></a>
  </div>
</section>

<section class="news">
  <div class="news-head">
    <h2>お知らせ</h2>
    <div class="en">NEWS</div>
    <a class="btn-list" href="#">お知らせ一覧<svg width="20" height="6" viewBox="0 0 20 6"><path d="M0 5h18L14 1" fill="none" stroke="#222" stroke-width="1"/></svg></a>
  </div>
  <ul class="news-list">
    <li><time>2023.10.15</time><p>こちらにテキストが入ります。テキストテキストテキストテキストテキスト。</p></li>
    <li><time>2023.10.10</time><p>こちらにテキストが入ります。テキストテキストテキストテキストテキスト。</p></li>
    <li><time>2023.09.25</time><p>こちらにテキストが入ります。テキストテキストテキストテキストテキスト。</p></li>
  </ul>
</section>

<section class="contact">
  <div class="photo" role="img" aria-label="火花が散る金属加工現場の写真"></div>
  <div class="contact-inner">
    <h2>CONTACT</h2>
    <p class="lead">ご質問・ご相談はお気軽に、どうぞお問い合わせください。</p>
    <div class="contact-boxes">
      <div class="cbox">
        <div><div class="tel">TEL.012-345-6789</div><small>受付時間 9:00〜17:00（土日祝を除く）</small></div>
      </div>
      <div class="cbox">
        <svg width="30" height="22" viewBox="0 0 30 22"><rect x="1" y="1" width="28" height="20" fill="none" stroke="#222" stroke-width="1.5"/><path d="M1 1l14 11L29 1" fill="none" stroke="#222" stroke-width="1.5"/></svg>
        <span class="mail">メールでのお問い合わせ</span>
      </div>
    </div>
  </div>
  <a class="to-top" href="#"><svg width="18" height="12" viewBox="0 0 18 12"><path d="M1 11L9 3l8 8" fill="none" stroke="#fff" stroke-width="2"/></svg></a>
</section>

<footer class="site-footer">
  <div class="logo">清良伸銅株式会社</div>
  <nav class="fnav">
    <a href="#">トップページ</a><a href="#">会社案内</a><a href="#">製造案内</a><a href="#">製品紹介</a><a href="#">採用情報</a>
    <a href="#">お知らせ</a><a href="#">お問い合わせ</a><a href="#">プライバシーポリシー</a><a href="#">サイトポリシー</a>
  </nav>
  <p class="copy">©Kiyora Shindo Co.,Ltd All Right Reserved.</p>
</footer>

</body>
</html>
```